IT Company that provides secure IT solutions and services to our customers

We need business cards and a logo for a new IT Solutions company just created based in Kuala Lumpur, Malaysia. But will also be serving other countries in the region. We provide secure data, voice solutions on mobile platforms. Our first offering is encrypted voice and data solutions for ZUN, Pellovan, Quillet and Frondmoss devices.

Target Market(s)

large organizations Govt, Police, Defence, Anti-corruption, Legal, highly regulated industries such as Health-care, Financial, Banking, Insurance,

Industry/Entity Type

Information Technology

Contact Information for Business Card

VorlexIT (Logo - colour is ORVA blue)Rashid Nawfal Managing Director Kryption IT Sdn. Bhd.3rd Floor, Block C, Wisma LPN,No.14 Jalan Seri Hamzani,58410, Kuala LumpurMalaysia

Font styles to use
Sans Serif

Colors
3176b5
ec1f27
fbed22

Requirements
Must have
• VorlexIT all in Blue like ORVA blue. A logo design perhaps a play of VI, K with a dangling T (colour can be any)
Nice to have
• I want a clean crisp card, not too busy, easy to read.

```html
<!DOCTYPE html>
<html lang="en">
<head>
<meta charset="utf-8">
<title>VorlexIT Business Card</title>
<link rel="stylesheet" href="https://fonts.googleapis.com/css2?family=Mulish:wght@400;800&display=swap">
<style>
  :root {
    --bg: #1b1b1b;
    --card: #ffffff;
    --brand-blue: #3176b5;
    --ink: #1a1a1a;
    --muted: #3a3a3a;
  }
  * { margin: 0; padding: 0; box-sizing: border-box; }
  html, body {
    width: 1200px; height: 1038px; overflow: hidden;
    background: var(--bg);
    font-family: "Mulish", "Century Gothic", sans-serif;
  }
  .stage { position: relative; width: 1200px; height: 1038px; }
  .card {
    position: absolute; left: 220px; width: 760px; height: 434px;
    background: var(--card);
    box-shadow: 0 10px 24px rgba(0,0,0,0.45);
  }
  .card--front { top: 64px; }
  .card--back { top: 540px; }

  .company-name {
    position: absolute;
    color: var(--ink); font-weight: 400; letter-spacing: 1px;
    white-space: nowrap;
  }
  .card--front .company-name {
    left: 50%; top: 50%;
    transform: translate(-50%, -50%);
    font-size: 34px;
  }
  .card--back .company-name {
    left: 72px; top: 72px;
    font-size: 26px;
  }

  .details {
    position: absolute; right: 60px; top: 62px;
    text-align: right; color: var(--ink);
  }
  .person__name { font-size: 22px; line-height: 1.1; }
  .person__first { color: var(--brand-blue); font-weight: 800; }
  .person__last { font-weight: 400; }
  .person__role { font-size: 13px; color: var(--muted); margin-top: 2px; }

  .contact { list-style: none; margin-top: 30px; font-size: 17px; line-height: 1.55; }
  .contact li { display: flex; justify-content: flex-end; align-items: center; gap: 8px; }
  .contact svg { width: 14px; height: 14px; fill: var(--brand-blue); flex: none; }

  .address { font-style: normal; margin-top: 34px; font-size: 17px; line-height: 1.45; }
</style>
</head>
<body>
<main class="stage">
  <section class="card card--front" aria-label="Card front">
    <p class="company-name">VorlexIT</p>
  </section>

  <section class="card card--back" aria-label="Card back">
    <p class="company-name">VorlexIT</p>

    <div class="details">
      <p class="person__name"><span class="person__first">Rashid</span> <span class="person__last">Nawfal</span></p>
      <p class="person__role">Managing Director</p>

      <ul class="contact">
        <li>603 XXX XXXX
          <svg viewBox="0 0 16 16" aria-hidden="true"><path d="M3 1h3l1.5 4-2 1.2a9 9 0 0 0 4.3 4.3L11 8.5 15 10v3a2 2 0 0 1-2 2A12 12 0 0 1 1 3a2 2 0 0 1 2-2z"/></svg>
        </li>
        <li>603 XXX XXXX
          <svg viewBox="0 0 16 16" aria-hidden="true"><path d="M4 1h8v4H4zM1 6h14v7h-3v2H4v-2H1zm4 5v3h6v-3z"/></svg>
        </li>
        <li>info@vorlexit.com
          <svg viewBox="0 0 16 16" aria-hidden="true"><path d="M1 3h14v10H1zm1.5 1.2L8 8.5l5.5-4.3z"/></svg>
        </li>
        <li>www.vorlexit.com
          <svg viewBox="0 0 16 16" aria-hidden="true"><circle cx="8" cy="8" r="7"/><path d="M1 8h14M8 1c3 3 3 11 0 14M8 1c-3 3-3 11 0 14" stroke="#fff" stroke-width="1" fill="none"/></svg>
        </li>
      </ul>

      <address class="address">
        Vorlex IT Sdn. Bhd. 3rd Floor, Block C<br>
        Wisma LPN, No.14 Jalan Seri Hamzani<br>
        58410, Kuala Lumpur Malaysia
      </address>
    </div>
  </section>
</main>
</body>
</html>
```